Tri Fold Brochure - Meridian Holding Circle

Pinecrest Partner Works LLC Meridian Holding Circle
Pinecrest Partner Works LLC also has a Meridian Holding Circle, administered by Senior Member Gregory Almsted. The Meridian Holding Circle gives select investors access to real estate opportunities across Florida’s desirable coastal counties. Our focus is on county tax deed sales, where properties may be acquired below estimated market value and offer potential for resale, rental income, redevelopment, or long-term growth.
Through market research, property analysis, and acquisition planning, we identify opportunities that are often missed through traditional real estate channels. Using local market insight and a disciplined tax deed strategy, our team targets properties in areas with strong tourism, population growth, economic activity, and steady demand for housing and commercial space.
Pinecrest Partner Works offers a collaborative platform where qualified opportunities that have been sourced and reviewed are presented to our Investors for participation. Instead of spending hours searching tax deed sales, investors gain access to these opportunities that have already undergone preliminary review. Profits from successful projects are shared among participating investors according to the terms of each opportunity.
Program Benefits
• Access to real estate opportunities identified through Florida tax deed sales
• Focus on high-demand coastal counties with strong tourism and economic activity
• Professional property sourcing and preliminary due diligence
• Opportunities to acquire properties below estimated market value
• Participation in a collaborative investment model
• Potential income through resale, redevelopment, rental, or appreciation
• Access to opportunities not readily available through traditional real estate markets
Whether you are an experienced investor or looking to diversify your portfolio, the Meridian Holding Circle offers a structured way to participate in Florida real estate opportunities.
Bayline Ventures is administered by Pinecrest Partner Works LLC. All investments involve risk, including possible loss of principal. Returns are not guaranteed, and past performance does not guarantee future results. Prospective investors should conduct their own due diligence and consult legal, tax, and financial advisors before making any investment decision.

Understanding Florida Tax Deed Sales
One of the unique advantages of investing in Florida tax deed properties is that Florida operates differently from most states throughout the United States. In many states, delinquent property taxes are sold as tax lien certificates, meaning investors purchase the debt against a property and earn interest while the property owner retains ownership rights. In Florida, however, once statutory requirements have been met and redemption periods have expired, properties may proceed to a Tax Deed Sale, where the actual real estate itself is auctioned to the highest bidder. This process can create opportunities for investors to acquire ownership of real property rather than simply holding a tax lien. Because many tax deed properties receive limited market exposure and are sold through county-administered auctions, acquisition prices may be significantly below estimated market value. For knowledgeable investors who understand the process and conduct proper due diligence, Florida's tax deed system can present unique opportunities not commonly available through traditional real estate acquisitions or tax lien investing programs found in other states.

What Happens After a Successful Tax Deed Purchase?
Once a property is successfully acquired at a Florida Tax Deed Sale, the process of securing ownership is often more straightforward than many investors expect. Unlike traditional real estate transactions that may involve lengthy negotiations, financing contingencies, inspections, appraisals, and extensive closing requirements, a tax deed purchase generally follows a streamlined county-administered process.
After the winning bid is submitted and the required funds are paid, the county clerk typically issues a Tax Deed conveying ownership rights to the successful bidder. The deed is then recorded in the public land records, establishing the investor's ownership interest in the property. In many cases, the administrative costs associated with recording and obtaining the deed are relatively modest when compared to traditional real estate acquisition expenses.
Following the recording of the Tax Deed, investors generally verify the property's status, including occupancy, municipal code compliance, utility availability, and any matters that may affect future use or marketability. Depending on the investment strategy, the property may then be prepared for resale, renovation, rental, redevelopment, or long-term holding.
For investors seeking the highest level of marketability and title assurance, a quiet title action may be pursued. A quiet title action is a legal process used to resolve potential claims or interests that may cloud title and can make the property more attractive to future buyers and lenders. While not every situation is identical, many investors view this as a routine step in maximizing a property's resale value and financing options.
One of the reasons Florida tax deed investing is attractive to many investors is that, after acquisition, the ownership transfer process is often largely administrative in nature. Rather than navigating months of traditional purchase negotiations and financing approvals, investors may be able to move directly into implementing their chosen investment strategy. With proper due diligence and professional guidance, the post-acquisition process can often be managed efficiently while positioning the property for future profit opportunities.
The procedures, costs, and timelines associated with Florida tax deed properties vary by county and property. Investors should consult qualified legal, title, tax, and real estate professionals before making investment decisions.

Why We Focus on Condominium Opportunities
Because Florida tax deed auctions are conducted online and many targeted properties are located hundreds of miles from our investors and acquisition team, it is often impractical to perform a comprehensive interior inspection prior to bidding. As a result, many tax deed properties throughout Florida are acquired based primarily on available public records, county information, satellite imagery, exterior observations, market data, and community research. To help manage risk in this environment, Bayline Ventures frequently prioritizes condominium opportunities located within established communities.
Condominiums often present several advantages when compared to single-family homes or vacant land acquisitions. Since the condominium association is typically responsible for maintaining the building exterior, roofs, common areas, landscaping, and many structural components, investors are generally exposed to fewer unknown repair items. In addition, condominium units often require less renovation work, lower capital expenditures, and shorter turnaround times to prepare for resale or rental occupancy. By focusing on properties with potentially lower rehabilitation costs and more predictable maintenance requirements, Bayline Ventures seeks to preserve profit margins while reducing the likelihood that unexpected repair expenses will significantly impact overall project performance.
While no investment is without risk, our emphasis on condominium communities is intended to create a more efficient acquisition strategy that aligns with the realities of online tax deed investing and helps promote disciplined investment decisions.

A Collaborative Investment Model
Pinecrest Partner Works LLC ("PPW") was founded on the principle that successful real estate investing is best achieved through collaboration. Each investment opportunity brings together qualified investors who combine financial resources, experience, and expertise to pursue carefully selected real estate acquisitions. Prior to participating in any venture, prospective investors undergo a thorough vetting process designed to promote responsible participation and help ensure that each investment group is comprised of financially capable and like-minded individuals.
For each investment opportunity, profits are generally distributed among the participating investors in proportion to their respective capital contributions, subject to the terms of the applicable Joint Venture Agreement. This structure provides a transparent and equitable framework that aligns each participant's financial interest with the overall success of the project.
Gregory Almsted, acting on behalf of Pinecrest Partner Works LLC, serves as the Senior Project Manager for each joint venture. In this role, Mr. Almsted oversees the acquisition process, project coordination, due diligence, renovation planning, investor communications, contractor coordination, disposition strategy, and overall project management from acquisition through final distribution. As compensation for these management services, Pinecrest Partner Works LLC generally receives a project management fee equal to five percent (5%) of the approved renovation budget, as specified in the applicable project agreements.
In addition, Pinecrest Partner Works LLC is granted the first opportunity, where permitted by law and agreed to by the joint venture participants, to provide mortgage financing and real estate brokerage services that may be required during the acquisition, refinancing, or disposition of a project. Any such services will be provided through appropriately licensed entities and disclosed in accordance with applicable federal and state laws.
Beyond project management, Pinecrest Partner Works LLC provides comprehensive administrative support for each venture, including entity formation and business registration (when applicable), preparation and coordination of legal documentation, maintenance of accounting records and bookkeeping, financial reporting, record retention, and general administrative oversight. This centralized management approach enables investors to focus on the investment opportunity while PPW coordinates the operational and administrative functions necessary to help each project proceed efficiently and professionally.

For more information, contact Gregory Almsted directly at (555) 284-9073 or gregory@ppwgroupmail.com

```html
<!DOCTYPE html>
<html lang="en">
<head>
<meta charset="utf-8">
<title>Meridian Holding Circle – Tri-Fold Brochure</title>
<link rel="stylesheet" href="https://fonts.googleapis.com/css2?family=Libre+Caslon+Display&family=Montserrat:ital,wght@0,400;0,500;0,600;0,700;1,400&display=swap">
<style>
:root{
  --backdrop:#d4d1d4;
  --ink:#050506;
  --gold:#c4a46a;
  --gold-deep:#6f6148;
  --mist:#e9f0f8;
  --paper:#ffffff;
  --text:#2a2c30;
  --muted:#55585e;
  --rule-dark:#2e2f33;
  --rule-light:#d3dbe5;
}
*{box-sizing:border-box;margin:0;padding:0}
html,body{width:1200px;height:3307px;overflow:hidden}
body{background:var(--backdrop);font-family:"Montserrat",Arial,sans-serif;color:var(--text);position:relative}

.label{font-size:10.5px;letter-spacing:1.6px;text-transform:uppercase;font-weight:500}
.title{font-family:"Libre Caslon Display",Georgia,serif;font-weight:400;font-size:17px;line-height:22px;margin-top:6px}
.body-copy{font-size:11px;line-height:16.5px}

/* cover panel */
.cover{position:absolute;width:354px;height:821px;background:var(--ink);overflow:hidden;color:#fff;text-align:center}
.cover-photo{position:absolute;left:0;top:0}
.brand{position:absolute;left:0;right:0;top:38px;display:flex;justify-content:center;align-items:center;gap:8px}
.brand-mark{width:12px;height:12px;background:var(--ink)}
.brand-name{font-weight:600;font-size:15px;letter-spacing:2.4px;color:var(--ink);line-height:20px;text-align:left}
.cover-kicker{position:absolute;left:0;right:0;top:506px;font-size:9px;letter-spacing:1.6px;font-weight:600}
.cover-title{position:absolute;left:0;right:0;top:526px;font-family:"Libre Caslon Display",Georgia,serif;font-weight:400;line-height:1}
.cover-title .gold{display:block;color:var(--gold);font-size:22px;letter-spacing:.5px}
.cover-title .big{display:block;font-size:40px;margin-top:6px;letter-spacing:.5px}
.cover-rule{position:absolute;left:157px;top:661px;width:40px;height:2px;background:var(--gold)}
.cover-lede{position:absolute;left:40px;right:40px;top:680px;font-size:11px;line-height:15px}
.cover-foot{position:absolute;left:0;right:0;top:794px;font-size:8.5px;font-weight:600}
.cover-foot span{margin:0 9px}
.cover-hero{left:299px;top:70px;transform:scale(1.7);transform-origin:0 0;box-shadow:0 18px 40px rgba(0,0,0,.25)}

/* spreads */
.spread{position:absolute;left:68px;width:1063px;height:821px;display:flex;box-shadow:0 6px 16px rgba(0,0,0,.18)}
.spread-out{top:1566px}
.spread-in{top:2431px}
.panel{position:relative;width:354px;height:821px;padding:47px 45px 0 45px;overflow:hidden}
.panel-dark{background:var(--ink);color:#fff}
.panel-mist{background:var(--mist)}
.panel-white{background:var(--paper)}
.panel-dark .title{color:var(--gold)}
.panel-white .title,.panel-mist .title{color:var(--ink)}

/* benefits */
.benefits{list-style:none;margin-top:16px}
.benefits li{font-size:11px;line-height:16px;padding:9px 0 10px 13px;border-bottom:1px solid var(--rule-dark);position:relative}
.benefits li:last-child{border-bottom:none}
.benefits li::before{content:"–";position:absolute;left:0}
.portrait{position:absolute;left:150px;top:540px}
.contact-card{position:absolute;left:0;top:616px;width:208px;height:174px;background:var(--gold-deep);padding:24px 0 0 45px;color:#fff}
.contact-name{font-family:"Libre Caslon Display",Georgia,serif;font-size:18px}
.contact-role{font-size:9px;font-weight:600;margin-top:3px}
.contact-lines{font-size:9.5px;line-height:16px;margin-top:12px}

/* how it works */
.callout{margin-top:22px;background:var(--paper);border-left:3px solid var(--gold);padding:14px 14px 14px 16px;font-style:italic;font-size:10.8px;line-height:16.5px;color:var(--muted)}
.section-tag{margin-top:28px}
.steps{list-style:none;margin-top:10px}
.step{display:flex;gap:14px;padding:10px 0 14px;border-bottom:1px solid var(--rule-light)}
.step:last-child{border-bottom:none}
.step svg{flex:none;margin-top:3px}
.step-title{font-size:12.5px;font-weight:500;color:var(--ink)}
.step-copy{font-size:10.6px;line-height:17px;color:var(--muted);margin-top:4px}

/* inside */
.photo{display:block}
.feature-list{list-style:none;margin-top:10px}
.feature{display:flex;gap:14px;background:var(--mist);padding:9px 10px 9px 12px;margin-bottom:4px;height:72px}
.feature svg{flex:none;margin-top:6px}
.feature-title{font-size:11.3px;font-weight:600;color:var(--ink)}
.feature-copy{font-size:9.6px;line-height:14px;color:var(--muted);margin-top:3px}
.split{display:flex;gap:14px;margin-top:16px}
.split .body-copy{font-size:10.8px;line-height:16px}
.quote-white{margin-top:16px;background:var(--paper);border-left:3px solid var(--gold);padding:12px 12px 12px 16px;font-style:italic;font-size:10.4px;line-height:16px;color:var(--muted)}
.closing{margin-top:14px;font-size:10.8px;line-height:16px}
.fee-box{margin-top:16px;background:var(--mist);padding:14px 16px 16px}
.fee-head{display:flex;align-items:center;gap:10px}
.fee-num{font-size:30px;font-weight:500;color:var(--ink)}
.fee-label{font-size:11px;font-weight:600;line-height:13px;color:var(--ink)}
.fee-copy{font-size:9.8px;line-height:15.5px;color:var(--muted);margin-top:10px}
.services-title{font-size:11px;font-weight:700;color:var(--ink);margin-top:14px}
.services{list-style:none;margin-top:4px}
.services li{font-size:10px;line-height:14px;padding:5px 6px;border-bottom:1px solid var(--rule-light);color:var(--muted)}
</style>
</head>
<body>

<!-- front cover, shown large -->
<section class="cover cover-hero" aria-label="Front cover">
  <svg class="cover-photo" width="354" height="500" viewBox="0 0 354 500" role="img" aria-label="Photo of a glass-balconied coastal high-rise beside palm trees, a pool and the ocean">
    <defs><linearGradient id="heroSky" x1="0" y1="0" x2="0" y2="1"><stop offset="0" stop-color="#b6dcf6"/><stop offset=".45" stop-color="#8cc3e8"/><stop offset="1" stop-color="#3b88b4"/></linearGradient></defs>
    <polygon points="19,0 335,0 335,440 177,492 19,440" fill="url(#heroSky)"/>
    <polyline points="19,440 177,492 335,440" fill="none" stroke="#c4a46a" stroke-width="3"/>
  </svg>
  <div class="brand"><span class="brand-mark"></span><span class="brand-name">PINECREST PARTNER<br>WORKS LLC</span></div>
  <p class="cover-kicker">MERIDIAN HOLDING CIRCLE</p>
  <h1 class="cover-title"><span class="gold">FLORIDA'S COASTAL</span><span class="big">REAL ESTATE</span><span class="big">OPPORTUNITY</span></h1>
  <span class="cover-rule"></span>
  <p class="cover-lede">Accessing coastal real estate opportunities through Florida's unique tax deed system — for qualified investors seeking returns beyond traditional markets</p>
  <p class="cover-foot">Tax Deed Acquisitions<span>|</span>Collaborative Investing</p>
</section>

<!-- outside spread -->
<section class="spread spread-out" aria-label="Outside spread">
  <div class="panel panel-dark">
    <p class="label">Program Benefits</p>
    <h2 class="title">Why Investors Choose Meridian</h2>
    <ul class="benefits">
      <li>Access to real estate opportunities identified through Florida tax deed sales.</li>
      <li>Focus on high-demand coastal counties with strong tourism &amp; economic activity.</li>
      <li>Professional property sourcing and preliminary due diligence.</li>
      <li>Opportunities to acquire properties below estimated market value.</li>
      <li>Participation in a collaborative investment model.</li>
      <li>Potential income through resale, redevelopment, rental, or appreciation.</li>
      <li>Access to opportunities unavailable through traditional real estate markets.</li>
      <li>Centralized administrative support — entity formation, legal docs, bookkeeping</li>
    </ul>
    <svg class="portrait" width="204" height="281" viewBox="0 0 204 281" role="img" aria-label="Portrait of the senior member seated, in a dark suit and hat">
      <defs><linearGradient id="portraitTone" x1="0" y1="0" x2="0" y2="1"><stop offset="0" stop-color="#050506"/><stop offset="1" stop-color="#2a2a2d"/></linearGradient></defs>
      <rect width="204" height="281" fill="url(#portraitTone)"/>
    </svg>
    <div class="contact-card">
      <p class="contact-name">Gregory Almsted</p>
      <p class="contact-role">(Senior Member)</p>
      <p class="contact-lines">Pinecrest Partner Works LLC<br>(555) 284-9073<br>gregory@ppwgroupmail.com</p>
    </div>
  </div>

  <div class="panel panel-mist">
    <p class="label">How It Works</p>
    <h2 class="title">Florida's Tax Deed Advantage</h2>
    <p class="body-copy" style="margin-top:16px;color:var(--muted)">Unlike most states where investors purchase tax liens, Florida allows the actual real estate to be auctioned once statutory requirements and redemption periods have expired. This means investors can acquire direct ownership — not just debt — often at prices well below estimated market value.</p>
    <p class="callout">Because many tax deed properties receive limited market exposure and are sold through county-administered auctions, acquisition prices may be significantly below estimated market value.</p>
    <p class="label section-tag">After Acquisition</p>
    <ol class="steps">
      <li class="step"><svg width="30" height="30" viewBox="0 0 30 30"><polygon points="15,1 28,8 28,22 15,29 2,22 2,8" fill="#050506"/><text x="15" y="19" text-anchor="middle" font-size="11" font-family="Montserrat,Arial,sans-serif" fill="#fff">1</text></svg><div><p class="step-title">Winning Bid &amp; Payment</p><p class="step-copy">Funds are submitted to the county; a Tax Deed is issued conveying ownership rights.</p></div></li>
      <li class="step"><svg width="30" height="30" viewBox="0 0 30 30"><polygon points="15,1 28,8 28,22 15,29 2,22 2,8" fill="#050506"/><text x="15" y="19" text-anchor="middle" font-size="11" font-family="Montserrat,Arial,sans-serif" fill="#fff">2</text></svg><div><p class="step-title">Deed Recorded</p><p class="step-copy">The deed is recorded in public land records, establishing the investor's ownership.</p></div></li>
      <li class="step"><svg width="30" height="30" viewBox="0 0 30 30"><polygon points="15,1 28,8 28,22 15,29 2,22 2,8" fill="#050506"/><text x="15" y="19" text-anchor="middle" font-size="11" font-family="Montserrat,Arial,sans-serif" fill="#fff">3</text></svg><div><p class="step-title">Property Status Review</p><p class="step-copy">Occupancy, code compliance, and utility availability are verified.</p></div></li>
      <li class="step"><svg width="30" height="30" viewBox="0 0 30 30"><polygon points="15,1 28,8 28,22 15,29 2,22 2,8" fill="#050506"/><text x="15" y="19" text-anchor="middle" font-size="11" font-family="Montserrat,Arial,sans-serif" fill="#fff">4</text></svg><div><p class="step-title">Strategy Execution</p><p class="step-copy">Property is prepared for resale, rental, renovation, or long-term holding.</p></div></li>
    </ol>
  </div>

  <section class="cover" style="position:relative" aria-label="Front cover">
    <svg class="cover-photo" width="354" height="500" viewBox="0 0 354 500" role="img" aria-label="Photo of a glass-balconied coastal high-rise beside palm trees, a pool and the ocean">
      <defs><linearGradient id="panelSky" x1="0" y1="0" x2="0" y2="1"><stop offset="0" stop-color="#b6dcf6"/><stop offset=".45" stop-color="#8cc3e8"/><stop offset="1" stop-color="#3b88b4"/></linearGradient></defs>
      <polygon points="19,0 335,0 335,440 177,492 19,440" fill="url(#panelSky)"/>
      <polyline points="19,440 177,492 335,440" fill="none" stroke="#c4a46a" stroke-width="3"/>
    </svg>
    <div class="brand"><span class="brand-mark"></span><span class="brand-name">PINECREST PARTNER<br>WORKS LLC</span></div>
    <p class="cover-kicker">MERIDIAN HOLDING CIRCLE</p>
    <h2 class="cover-title"><span class="gold">FLORIDA'S COASTAL</span><span class="big">REAL ESTATE</span><span class="big">OPPORTUNITY</span></h2>
    <span class="cover-rule"></span>
    <p class="cover-lede">Accessing coastal real estate opportunities through Florida's unique tax deed system — for qualified investors seeking returns beyond traditional markets</p>
    <p class="cover-foot">Tax Deed Acquisitions<span>|</span>Collaborative Investing</p>
  </section>
</section>

<!-- inside spread -->
<section class="spread spread-in" aria-label="Inside spread">
  <div class="panel panel-white">
    <p class="label">Acquisition Strategy</p>
    <h2 class="title">Why We Focus on Condominium Opportunities</h2>
    <p class="body-copy" style="margin-top:12px;color:var(--muted)">Because Florida tax deed auctions are conducted online and many target properties are located hundreds of miles away, comprehensive interior inspections prior to bidding are often impractical. Condominiums within established communities offer a more measurable risk profile.</p>
    <svg class="photo" style="margin-top:12px" width="264" height="130" viewBox="0 0 264 130" role="img" aria-label="Photo of a bright condominium living room with ocean-view windows">
      <defs><linearGradient id="livingTone" x1="0" y1="0" x2="0" y2="1"><stop offset="0" stop-color="#b9cfe0"/><stop offset=".55" stop-color="#e6e2dc"/><stop offset="1" stop-color="#8d7a67"/></linearGradient></defs>
      <rect width="264" height="130" fill="url(#livingTone)"/>
    </svg>
    <ul class="feature-list">
      <li class="feature"><svg width="36" height="36" viewBox="0 0 36 36" fill="none" stroke="#c4a46a" stroke-width="1.4"><circle cx="19" cy="12" r="8"/><path d="M4 28h8l6 3 12-6M4 24h7l7 2"/></svg><div><p class="feature-title">Lower Rehab Costs</p><p class="feature-copy">Associations handle roofs, exteriors, &amp; common areas — reducing unknown repair items.</p></div></li>
      <li class="feature"><svg width="36" height="36" viewBox="0 0 36 36" fill="none" stroke="#c4a46a" stroke-width="1.4"><circle cx="18" cy="19" r="13"/><path d="M18 11v8l6 4"/></svg><div><p class="feature-title">Faster Turnaround</p><p class="feature-copy">Less renovation typically means shorter timelines to resale or rental readiness.</p></div></li>
      <li class="feature"><svg width="36" height="36" viewBox="0 0 36 36" fill="none" stroke="#c4a46a" stroke-width="1.4"><rect x="4" y="6" width="24" height="22" rx="2"/><path d="M4 12h24M10 3v6M22 3v6"/><circle cx="26" cy="26" r="6"/></svg><div><p class="feature-title">Predictable Maintenance</p><p class="feature-copy">Structural components covered by HOA — fewer surprise capital expenditures.</p></div></li>
      <li class="feature"><svg width="36" height="36" viewBox="0 0 36 36" fill="none" stroke="#c4a46a" stroke-width="1.4"><path d="M6 32V14M12 32V8M6 14l3-4 3 4"/><circle cx="24" cy="24" r="8"/><path d="M21 27l6-6"/></svg><div><p class="feature-title">Preserved Margins</p><p class="feature-copy">Disciplined approach aligns with online acquisition realities to protect project returns.</p></div></li>
    </ul>
    <p class="body-copy" style="margin-top:8px;color:var(--muted);font-size:10.8px;line-height:16px">While no investment is without risk, our emphasis on condominium communities is intended to create a more efficient acquisition strategy that promotes disciplined investment decisions.</p>
  </div>

  <div class="panel panel-dark">
    <p class="label">About the Program</p>
    <h2 class="title">The Meridian Holding Circle</h2>
    <div class="split">
      <svg width="122" height="173" viewBox="0 0 122 173" style="flex:none" role="img" aria-label="Photo of a waterfront high-rise skyline and bay">
        <defs><linearGradient id="bayTone" x1="0" y1="0" x2="0" y2="1"><stop offset="0" stop-color="#9ec6e6"/><stop offset=".6" stop-color="#5e8fb0"/><stop offset="1" stop-color="#2e5f80"/></linearGradient></defs>
        <rect width="122" height="173" fill="url(#bayTone)"/>
      </svg>
      <p class="body-copy">Administered by Senior Member Gregory Almsted, the Meridian Holding Circle gives select investors access to real estate opportunities across Florida's desirable coastal counties, sourced through county tax deed sales.</p>
    </div>
    <div class="split" style="margin-top:12px">
      <p class="body-copy">Through market research, property analysis, &amp; acquisition planning, we identify opportunities often missed through traditional real estate channels — leveraging local market insight &amp; disciplined tax deed strategy targeting areas with strong tourism, population growth, &amp; steady housing demand.</p>
      <svg width="122" height="222" viewBox="0 0 122 222" style="flex:none" role="img" aria-label="Photo of a beachfront condominium tower with pool and ocean">
        <defs><linearGradient id="towerTone" x1="0" y1="0" x2="0" y2="1"><stop offset="0" stop-color="#7fb7e6"/><stop offset=".5" stop-color="#e8e1d3"/><stop offset="1" stop-color="#6ea8c0"/></linearGradient></defs>
        <rect width="122" height="222" fill="url(#towerTone)"/>
      </svg>
    </div>
    <p class="quote-white">Investors gain access to opportunities that have already undergone preliminary review, rather than spending hours searching tax deed sales themselves. Profits are shared among participating investors according to the terms of each opportunity.</p>
    <p class="body-copy closing">Whether you are an experienced investor or looking to diversify your portfolio, the Meridian Holding Circle offers a structured way to participate in Florida real estate opportunities.</p>
  </div>

  <div class="panel panel-white">
    <p class="label">Investment Structure</p>
    <h2 class="title">A Collaborative Model Built on Transparency</h2>
    <p class="body-copy" style="margin-top:12px;color:var(--muted)">Profits are distributed among participating investors in proportion to their respective capital contributions, subject to the terms of each Joint Venture Agreement. Prior to participating, prospective investors undergo a thorough vetting process.</p>
    <div class="fee-box">
      <div class="fee-head"><span class="fee-num">5%</span><span class="fee-label">Project<br>Management Fee</span></div>
      <p class="fee-copy">The approved renovation budget, as specified in each project agreement. PPW also holds first opportunity to provide mortgage financing &amp; brokerage services where permitted.</p>
    </div>
    <p class="services-title">PPW Administrative Services Include</p>
    <ul class="services">
      <li>Entity formation &amp; business registration</li>
      <li>Legal documentation preparation &amp; coordination</li>
      <li>Accounting records &amp; bookkeeping</li>
      <li>Financial reporting &amp; record retention</li>
      <li>Acquisition, renovation &amp; disposition oversight</li>
    </ul>
    <svg class="photo" style="margin-top:30px" width="264" height="200" viewBox="0 0 264 200" role="img" aria-label="Aerial photo of beachfront condominium towers along the coast">
      <defs><linearGradient id="aerialTone" x1="0" y1="0" x2="0" y2="1"><stop offset="0" stop-color="#a9c9e3"/><stop offset=".55" stop-color="#5f86a3"/><stop offset=".8" stop-color="#d9cfb9"/><stop offset="1" stop-color="#4f9ab8"/></linearGradient></defs>
      <rect width="264" height="200" fill="url(#aerialTone)"/>
    </svg>
  </div>
</section>

</body>
</html>
```